Marist Valley College Brenthurst Letterhead

Our college is called Marist Valley College Brenthurst. We would like to request a few letterhead design options to choose from please. We look forward to seeing some new and fresh ideas for our College Letterhead.

Please note that the College has the following PMS Colours:
MAROON – PMS 229C
BLUE – PMS 2747C
GOLD – PMS 871C
YELLOW – PMS 123C

Our College Motto is:
Faith seeking Understanding.
I have attached a copy of our current letterhead and College Logo.

Please note that the letterhead must include the following details:

Marist Valley College Brenthurst
Faith Seeking Understanding
Phone: 8472 5518
Fax:8415 7730
Address: 214 Kellaway Street Brenthurst 3041
Mail:PO BOX 4857 Marlow Heights VIC 3045 Australia
ABN 61 507 284 913

www.mvcbrenthurst-example.net
https://twitter.com/mvcbrenthurst
https://www.pinterest.com/mvcbrenthurst
https://www.facebook.com/MVCBrenthurst
www.youtube.com (search MVC Brenthurst)

Please feel free to contact me on the below detail if I can further assist.

Regards,
Joanna Whitcombe
reception@mvcbrenthurst-example.net
PH: 8472 5518

Target Market(s)

College Community

Industry/Entity Type

Education

Font styles to use
Other font styles liked:
• You decide

Requirements
Must have
• See Project Description
Nice to have
• see Project Description

```html
<!DOCTYPE html>
<html lang="en">
<head>
<meta charset="utf-8">
<title>Marist Valley College Brenthurst Letterhead</title>
<link href="https://fonts.googleapis.com/css2?family=Source+Sans+3:wght@400;600&display=swap" rel="stylesheet">
<style>
  :root {
    --backdrop: #aaa8a9;
    --paper: #f5f4f2;
    --maroon: #8a2035;
    --navy: #172a52;
    --gold: #f2c42a;
    --ink: #4a4a4a;
    --ink-soft: #555555;
    --rule: #c9c9c9;
  }
  * { box-sizing: border-box; margin: 0; padding: 0; }
  html, body {
    width: 989px; height: 1200px; overflow: hidden;
    background: var(--backdrop);
    font-family: "Source Sans 3", "Myriad Pro", Arial, sans-serif;
    color: var(--ink);
  }
  .letterhead {
    position: absolute; left: 70px; top: 0;
    width: 849px; height: 1200px;
    background: var(--paper);
  }
  .college-mark {
    position: absolute; left: 85px; top: 92px;
    display: flex; align-items: center; gap: 12px;
  }
  .college-mark__dot {
    width: 34px; height: 34px; border-radius: 50%;
    background: var(--maroon); flex: none;
  }
  .college-mark__name {
    font-size: 19px; font-weight: 600; line-height: 1.15;
    color: var(--navy); width: 170px;
  }
  .contact-address {
    position: absolute; right: 236px; top: 84px;
    text-align: right; font-size: 12.5px; line-height: 16.5px;
    color: var(--ink-soft);
  }
  .contact-address p + p { margin-top: 4px; }
  .contact-address strong, .contact-lines strong { font-weight: 600; color: var(--ink); }
  .contact-divider {
    position: absolute; left: 632px; top: 88px;
    width: 1px; height: 74px; background: var(--rule);
  }
  .contact-lines {
    position: absolute; left: 650px; top: 84px;
    font-size: 12.5px; line-height: 16.5px; color: var(--ink-soft);
    list-style: none;
  }
  .contact-lines li { display: flex; align-items: center; gap: 6px; }
  .contact-lines svg { width: 12px; height: 12px; fill: var(--navy); flex: none; }
  .salutation {
    position: absolute; left: 84px; top: 318px;
    font-size: 23px; font-weight: 400; color: var(--ink-soft);
  }
  .letter-body {
    position: absolute; left: 84px; top: 386px; width: 686px;
    font-size: 13px; line-height: 20.6px; color: var(--ink);
    text-align: justify; hyphens: auto;
  }
  .letter-body p + p { margin-top: 20.6px; }
  .sign-off {
    position: absolute; left: 84px; top: 820px;
    font-size: 13px; color: var(--ink);
  }
  .signature {
    position: absolute; left: 79px; top: 852px;
    width: 113px; height: 43px;
    background: linear-gradient(90deg, rgba(23,42,82,0.12), rgba(23,42,82,0.28), rgba(23,42,82,0.1));
    border-radius: 4px;
  }
  .signatory {
    position: absolute; left: 88px; top: 910px;
    font-size: 14px; line-height: 22px; color: var(--ink-soft);
  }
  .footer-band {
    position: absolute; left: 0; top: 1145px;
    width: 100%; height: 34px;
    background: linear-gradient(90deg, var(--maroon) 0 710px, var(--navy) 710px 100%);
  }
  .footer-band__handle {
    position: absolute; left: 0; right: 0; top: 0;
    text-align: center; line-height: 34px;
    font-size: 12.5px; color: #ffffff;
  }
  .footer-band__dot {
    position: absolute; left: 676px; top: -6px;
    width: 26px; height: 26px; border-radius: 50%;
    background: var(--navy); border: 3px solid var(--gold);
  }
</style>
</head>
<body>
  <main class="letterhead">
    <header>
      <div class="college-mark">
        <span class="college-mark__dot"></span>
        <span class="college-mark__name">Marist Valley College Brenthurst</span>
      </div>

      <div class="contact-address">
        <p><strong>Address:</strong> 214 Kellaway Street<br>Brenthurst 3041</p>
        <p><strong>Mail:</strong> PO BOX 4857 Marlow<br>Heights VIC 3045 Australia</p>
      </div>

      <div class="contact-divider"></div>

      <ul class="contact-lines">
        <li><strong>ABN:</strong> 61 507 284 913</li>
        <li>
          <svg viewBox="0 0 24 24" aria-hidden="true"><path d="M6.6 10.8a15.1 15.1 0 0 0 6.6 6.6l2.2-2.2c.3-.3.7-.4 1-.2 1.1.4 2.3.6 3.6.6.6 0 1 .4 1 1V20c0 .6-.4 1-1 1A17 17 0 0 1 3 4c0-.6.4-1 1-1h3.5c.6 0 1 .4 1 1 0 1.3.2 2.5.6 3.6.1.3 0 .7-.2 1z"/></svg>
          8472 5518
        </li>
        <li>
          <svg viewBox="0 0 24 24" aria-hidden="true"><path d="M2 5h20v14H2z" fill="none"/><path d="M2 5h20v2l-10 6L2 7zM2 9l10 6 10-6v10H2z"/></svg>
          8415 7730
        </li>
        <li>
          <svg viewBox="0 0 24 24" aria-hidden="true"><circle cx="12" cy="12" r="10"/><path d="M2 12h20M12 2c3 3 3 17 0 20M12 2c-3 3-3 17 0 20" stroke="#f5f4f2" stroke-width="1.4" fill="none"/></svg>
          mvcbrenthurst-example.net
        </li>
      </ul>
    </header>

    <h1 class="salutation">Dear Mr. Harrow,</h1>

    <section class="letter-body">
      <p>Lorem ipsum dolor sit amet, consectetur adipiscing elit. Donec orci purus, luctus vitae dignissim eu, iaculis sed purus. Vivamus faucibus, ipsum nec aliquet viverra, leo mauris condimentum ligula, sit amet sagittis enim ligula quis arcu. Nam egestas tortor id nisi porttitor mattis. In tortor ante, ultricies in suscipit a, tempus non massa. Vivamus et auctor mi. Fusce vel massa nulla. Phasellus nec eros mauris, et scelerisque orci.</p>
      <p>Donec malesuada orci vitae nulla accumsan porta a id massa. Quisque accumsan iaculis magna sit amet fringilla. Maecenas consequat, magna eget tincidunt semper, odio nibh rutrum mi, id feugiat ante nisi eu risus. Vestibulum nunc orci, rhoncus a placerat in, ultricies in mi. Cras mattis varius eros, vel fringilla nisi suscipit eget. Quisque scelerisque sagittis nulla at porttitor.</p>
      <p>Sed id augue vitae urna euismod commodo aliquet a quam. Pellentesque arcu velit, cursus et malesuada ut, consequat et diam. Nullam erat sem, rhoncus id ullamcorper vitae, rhoncus et arcu. In ultricies ultricies nulla, ut rutrum nisi iaculis at. Donec eu magna a metus ornare faucibus. Fusce aliquet faucibus ultricies. Morbi semper, est id tincidunt gravida, sem arcu adipiscing lacus, ac bibendum nulla leo eu purus. Quisque nec diam sed risus consectetur accumsan quis quis nibh. Vestibulum id purus lorem.</p>
      <p>It is a long established fact that a reader will be distracted by the readable content of a page when looking at its layout. The point of using Lorem Ipsum is that it has a more-or-less normal distribution of letters, as opposed to using 'Content here, content here', making it look like readable English. Many desktop publishing packages</p>
    </section>

    <p class="sign-off">Sincerely,</p>
    <div class="signature" role="img" aria-label="Handwritten signature"></div>
    <p class="signatory">Daniel Harrow<br>CEO/ Founder</p>

    <footer class="footer-band">
      <span class="footer-band__handle">MVCBrenthurst</span>
      <span class="footer-band__dot"></span>
    </footer>
  </main>
</body>
</html>
```